Business Card for Dental Office

Our office is in the Hillcrest section of San Diego, California which is a well-established area. Maybe the back can be a map of our office location

```html
<!DOCTYPE html>
<html lang="en">
<head>
<meta charset="utf-8">
<title>Marston Dental – Business Card</title>
<link href="https://fonts.googleapis.com/css2?family=Open+Sans:wght@400;600;700&display=swap" rel="stylesheet">
<style>
  :root {
    --ink: #161616;
    --paper: #ffffff;
    --backdrop: #e9e6e1;
    --rule: #2a2a2a;
    --muted: #333333;
  }
  * { box-sizing: border-box; margin: 0; padding: 0; }
  html, body { width: 1200px; height: 900px; overflow: hidden; }
  body {
    background: var(--backdrop);
    font-family: "Open Sans", Arial, sans-serif;
    color: var(--ink);
    position: relative;
  }
  .card {
    position: absolute;
    width: 680px;
    height: 388px;
    background: var(--paper);
    box-shadow: 0 6px 18px rgba(0,0,0,.18);
    overflow: hidden;
  }
  .card--back { left: 440px; top: 40px; }
  .card--front { left: 80px; top: 472px; }

  /* Brand name block (both sides) */
  .brand {
    position: absolute;
    display: flex;
    align-items: center;
    gap: 12px;
  }
  .brand__mark {
    width: 18px; height: 18px;
    border-radius: 50%;
    background: var(--ink);
  }
  .brand__name {
    font-size: 34px;
    font-weight: 600;
    letter-spacing: .5px;
    color: var(--ink);
  }
  .card--back .brand { right: 60px; top: 120px; }
  .card--front .brand { right: 70px; top: 170px; }

  /* Appointment side */
  .appointment {
    position: absolute;
    left: 60px; top: 110px;
    width: 360px;
    font-weight: 700;
    font-size: 17px;
  }
  .appointment__title { font-size: 19px; margin-bottom: 20px; }
  .appointment__row {
    display: flex;
    align-items: flex-end;
    margin-bottom: 22px;
  }
  .appointment__line {
    flex: 1;
    border-bottom: 1.5px solid var(--rule);
    margin-left: 4px;
    height: 18px;
  }
  .appointment__line--short { flex: 0 0 150px; margin-right: 8px; }

  /* Contact side */
  .identity {
    position: absolute;
    left: 0; top: 26px;
    display: flex;
    align-items: flex-start;
    gap: 14px;
  }
  .identity__badge { width: 62px; height: 46px; display: block; }
  .identity__name { font-size: 22px; font-weight: 700; line-height: 1.1; margin-top: 4px; }
  .identity__role { font-size: 14px; color: var(--muted); }

  .contact {
    position: absolute;
    left: 40px; top: 150px;
    font-size: 15.5px;
    line-height: 1.45;
    list-style: none;
  }
  .contact__address { margin-bottom: 4px; }
  .contact__item { display: flex; align-items: center; gap: 10px; }
  .contact__icon { width: 12px; height: 12px; flex: none; }

  .footer-band {
    position: absolute;
    left: 0; bottom: 0;
    width: 680px; height: 70px;
    display: block;
  }
</style>
</head>
<body>

  <section class="card card--back" aria-label="Appointment side">
    <div class="appointment">
      <p class="appointment__title">Appointment</p>
      <div class="appointment__row">Name<span class="appointment__line"></span></div>
      <div class="appointment__row">Date<span class="appointment__line appointment__line--short"></span>Time<span class="appointment__line"></span></div>
    </div>
    <div class="brand">
      <span class="brand__mark"></span>
      <span class="brand__name">Marston Dental</span>
    </div>
  </section>

  <section class="card card--front" aria-label="Contact side">
    <div class="identity">
      <svg class="identity__badge" viewBox="0 0 62 46" aria-hidden="true">
        <rect width="62" height="46" fill="var(--ink)"/>
        <polygon points="32,0 38,0 22,46 16,46" fill="var(--paper)"/>
      </svg>
      <div>
        <p class="identity__name">Daniel Reyes</p>
        <p class="identity__role">Managing Director</p>
      </div>
    </div>

    <ul class="contact">
      <li class="contact__address">12345, Address Goes Here<br>Country Name, 123456.</li>
      <li class="contact__item">
        <svg class="contact__icon" viewBox="0 0 12 12" aria-hidden="true"><path d="M2.5 1 4.5 1 5.3 3.5 4 4.5Q5 7 7.5 8L8.5 6.7 11 7.5 11 9.5Q10.5 11 9 11 1 10 1 3 1 1.5 2.5 1Z" fill="var(--ink)"/></svg>
        044-123 456 789
      </li>
      <li class="contact__item">
        <svg class="contact__icon" viewBox="0 0 12 12" aria-hidden="true"><rect x="1" y="2.5" width="10" height="7" fill="var(--ink)"/><path d="M1 2.5 6 6.5 11 2.5" stroke="var(--paper)" fill="none" stroke-width="1"/></svg>
        info@marstondental.com
      </li>
      <li class="contact__item">
        <svg class="contact__icon" viewBox="0 0 12 12" aria-hidden="true"><path d="M5 7 7 5M4 5.5 2.5 7a2 2 0 0 0 2.5 2.5L6.5 8M8 6.5 9.5 5A2 2 0 0 0 7 2.5L5.5 4" stroke="var(--ink)" stroke-width="1.3" fill="none" stroke-linecap="round"/></svg>
        www.marstondental.com
      </li>
    </ul>

    <div class="brand">
      <span class="brand__mark"></span>
      <span class="brand__name">Marston Dental</span>
    </div>

    <svg class="footer-band" viewBox="0 0 680 70" preserveAspectRatio="none" aria-hidden="true">
      <polygon points="0,34 300,34 292,70 0,70" fill="var(--ink)"/>
      <polygon points="312,16 680,16 680,70 300,70" fill="var(--ink)"/>
    </svg>
  </section>

</body>
</html>
```